Business Card Design

I need business cards designed for a new company i have started that makes cakes, particularly themed kids cakes with a really modern design and I would like to have my business cards reflect this. I have attached some photos of cakes I have made and would like some to be used.

Industry/Entity Type

Business

Contact Information for Business Card

Business Name: Frosting and Treats by Norah
Mobile: 0427 519 863
email: norah@frostingandtreatsbynorah.com.au
Instagram: instagram.com/frostingandtreatsbynorah/
Facebook: fb.me/frostingandtreatsbynorah

Colors
e667a6
b768aa
3276b5

Requirements
Must have
• Business Name: Frosting and Treats by Norah
• Mobile: 0427 519 863
• email: norah@frostingandtreatsbynorah.com.au
• Instagram: instagram.com/frostingandtreatsbynorah/
• Facebook: fb.me/frostingandtreatsbynorah
Nice to have
• 2 to 3 pictures of my cakes

```html
<!DOCTYPE html>
<html lang="en">
<head>
<meta charset="utf-8">
<title>Frosting and Treats by Norah – Business Card</title>
<link rel="stylesheet" href="https://fonts.googleapis.com/css2?family=Roboto:wght@400;700&display=swap">
<style>
  :root {
    --page-bg: #e9e7e4;
    --card-bg: #ffffff;
    --brand-pink: #e667a6;
    --brand-gold: #d2c54e;
    --ink-grey: #6a6a6a;
    --on-pink: #ffffff;
  }
  * { box-sizing: border-box; margin: 0; padding: 0; }
  html, body {
    width: 1200px;
    height: 950px;
    overflow: hidden;
    background: var(--page-bg);
    font-family: "Roboto", Arial, sans-serif;
  }
  .sheet {
    width: 1200px;
    height: 950px;
    display: flex;
    flex-direction: column;
    align-items: center;
    justify-content: center;
    gap: 40px;
  }
  .card {
    position: relative;
    width: 760px;
    height: 434px;
    background: var(--card-bg);
    box-shadow: 0 6px 18px rgba(0,0,0,0.18);
    overflow: hidden;
  }
  .brand {
    display: flex;
    align-items: center;
    gap: 12px;
    color: var(--brand-pink);
    font-weight: 400;
    line-height: 1.1;
    white-space: nowrap;
  }
  .brand-dot {
    flex: none;
    border-radius: 50%;
    background: var(--brand-pink);
  }
  .card--front .brand {
    position: absolute;
    left: 50%;
    top: 50%;
    transform: translate(-50%, -50%);
    font-size: 40px;
  }
  .card--front .brand-dot { width: 26px; height: 26px; }
  .card--back .brand {
    position: absolute;
    left: 50px;
    top: 120px;
    font-size: 26px;
  }
  .card--back .brand-dot { width: 18px; height: 18px; }
  .wave {
    position: absolute;
    inset: 0;
    width: 100%;
    height: 100%;
  }
  .holder {
    position: absolute;
    right: 48px;
    top: 26px;
    text-align: right;
  }
  .holder-name {
    color: var(--brand-pink);
    font-weight: 700;
    font-size: 26px;
  }
  .holder-role {
    color: var(--ink-grey);
    font-size: 18px;
    margin-top: 2px;
  }
  .contacts {
    position: absolute;
    right: 40px;
    top: 212px;
    list-style: none;
    color: var(--on-pink);
    font-size: 14px;
  }
  .contact {
    display: flex;
    justify-content: flex-end;
    align-items: center;
    gap: 10px;
    height: 28px;
    white-space: nowrap;
  }
  .contact-icon {
    width: 16px;
    height: 16px;
    flex: none;
  }
</style>
</head>
<body>
<main class="sheet">
  <section class="card card--front" aria-label="Card front">
    <div class="brand"><span class="brand-dot"></span><span>Frosting and Treats<br>by Norah</span></div>
  </section>

  <section class="card card--back" aria-label="Card back">
    <svg class="wave" viewBox="0 0 760 434" preserveAspectRatio="none" aria-hidden="true">
      <path d="M0,388 C200,400 280,312 340,222 C400,137 560,96 760,92 L760,434 L0,434 Z" fill="var(--brand-gold)"/>
      <path d="M0,404 C210,416 290,328 350,238 C410,152 570,118 760,114 L760,434 L0,434 Z" fill="var(--card-bg)"/>
      <path d="M0,416 C220,428 300,340 360,250 C420,165 580,132 760,128 L760,434 L0,434 Z" fill="var(--brand-pink)"/>
    </svg>

    <div class="brand"><span class="brand-dot"></span><span>Frosting and Treats<br>by Norah</span></div>

    <header class="holder">
      <h1 class="holder-name">Norah Whitfield</h1>
      <p class="holder-role">Cake Designer</p>
    </header>

    <ul class="contacts">
      <li class="contact">
        <span>0427 519 863</span>
        <svg class="contact-icon" viewBox="0 0 18 18" aria-hidden="true"><rect x="4" y="1" width="10" height="16" rx="2" fill="none" stroke="#fff" stroke-width="1.6"/><circle cx="9" cy="14" r="1" fill="#fff"/></svg>
      </li>
      <li class="contact">
        <span>norah@frostingandtreatsbynorah.com.au</span>
        <svg class="contact-icon" viewBox="0 0 18 18" aria-hidden="true"><rect x="1" y="4" width="16" height="11" fill="none" stroke="#fff" stroke-width="1.6"/><path d="M1,4 L9,10 L17,4" fill="none" stroke="#fff" stroke-width="1.6"/></svg>
      </li>
      <li class="contact">
        <span>frostingandtreatsbynorah</span>
        <svg class="contact-icon" viewBox="0 0 18 18" aria-hidden="true"><rect x="1" y="1" width="16" height="16" rx="2" fill="#fff"/></svg>
      </li>
      <li class="contact">
        <span>frostingandtreatsbynorah</span>
        <svg class="contact-icon" viewBox="0 0 18 18" aria-hidden="true"><rect x="1" y="1" width="16" height="16" rx="2" fill="#fff"/></svg>
      </li>
    </ul>
  </section>
</main>
</body>
</html>
```